Lumi-Leaf Label for the Tea Tins and Boxes

We need a label design for our tea company. Our company promotes natural beauty from the inside out. We have many single and blended tea's that target specific markets, ie. weight loss, anti aging, healthy skin/hair etc. I want this design to attract ages 21 to 65. We need the label to be a white background with colour and black accents. We would like the use of herbs as the background.

Target Market(s)

attract ages 21 to 65. .

Industry/Entity Type

It Company

Font styles to use
Serif
Decorative

Colors
f78f20
ffffff
9bcb3c
0792cd
fbed22

Requirements
Must have
• we must have a clean design
Nice to have
• Color with black accents
Should not have
• busy design

```html
<!DOCTYPE html>
<html lang="en">
<head>
<meta charset="utf-8">
<title>Lumi-Leaf Co. — Green Tea Label</title>
<link rel="stylesheet" href="https://fonts.googleapis.com/css2?family=Sorts+Mill+Goudy&display=swap">
<style>
  :root {
    --label-white: #ffffff;
    --ink-black: #141414;
    --text-grey: #4a4a4a;
    --leaf-green: #5cc43a;
    --leaf-green-soft: #a9dd8a;
    --leaf-green-pale: #eef7e8;
  }
  * { margin: 0; padding: 0; box-sizing: border-box; }
  html, body {
    width: 1200px;
    height: 1200px;
    overflow: hidden;
    background: var(--label-white);
  }
  .tea-label {
    position: relative;
    width: 1200px;
    height: 1200px;
    background: var(--label-white);
    font-family: "Sorts Mill Goudy", "Goudy Old Style", Georgia, serif;
  }
  .watercolour-badge {
    position: absolute;
    left: 145px;
    top: 120px;
    width: 910px;
    height: 910px;
  }
  .brand-name {
    position: absolute;
    left: 0;
    width: 1200px;
    top: 470px;
    text-align: center;
    font-size: 74px;
    letter-spacing: 1px;
    color: var(--ink-black);
    display: flex;
    justify-content: center;
    align-items: center;
    gap: 22px;
  }
  .brand-dot {
    width: 22px;
    height: 22px;
    border-radius: 50%;
    background: var(--ink-black);
  }
  .blend-description {
    position: absolute;
    left: 0;
    width: 1200px;
    top: 645px;
    text-align: center;
    font-size: 34px;
    line-height: 48px;
    letter-spacing: 1px;
    text-transform: uppercase;
    color: var(--text-grey);
  }
  .net-weight {
    position: absolute;
    left: 0;
    width: 1200px;
    top: 1085px;
    text-align: center;
    font-size: 34px;
    color: var(--text-grey);
  }
</style>
</head>
<body>
  <main class="tea-label">
    <svg class="watercolour-badge" viewBox="0 0 910 910" role="img" aria-label="Soft green watercolour wash framed by a hand-painted green ring">
      <defs>
        <radialGradient id="wash-fill" cx="50%" cy="45%" r="50%">
          <stop offset="0%" stop-color="var(--leaf-green-pale)"/>
          <stop offset="55%" stop-color="#d6efc6"/>
          <stop offset="100%" stop-color="var(--leaf-green-soft)"/>
        </radialGradient>
      </defs>
      <circle cx="455" cy="450" r="345" fill="url(#wash-fill)"/>
      <circle cx="455" cy="455" r="425" fill="none" stroke="var(--leaf-green)" stroke-width="38" opacity="0.85"/>
    </svg>

    <h1 class="brand-name"><span class="brand-dot"></span>Lumi-Leaf Co.</h1>

    <p class="blend-description">
      Refreshing Green<br>
      Tea Blend &amp; Extra Large<br>
      Wire Mesh Filter
    </p>

    <p class="net-weight">3oz Net Wt (85g)</p>
  </main>
</body>
</html>
```